New business card for civil engineering company - "Keystone Audit"

We need a business card designed for our new structural engineering company.

The company name is "Keystone Audit" logo files attached.

We would like the following:
* Two-sided card
* Simple design

Information to be placed on the card:
Name - Marcus Dellow
Job Title - Director / Structural Engineer
Credentials - BEng(Hons), CPEng, CMengNZ, IntPE(NZ)
Email - marcus.dellow@keystoneaudit.co.nz
mobile - 0219364058
website - www.keystoneaudit.co.nz

```html
<!DOCTYPE html>
<html lang="en">
<head>
<meta charset="utf-8">
<title>Keystone Audit — Business Card</title>
<link rel="stylesheet" href="https://fonts.googleapis.com/css2?family=Questrial&display=swap">
<style>
  :root {
    --backdrop: #2a2a2c;
    --brand-blue: #0f74bd;
    --panel-grey: #e6e7e9;
    --ink-dark: #3b3c3e;
    --white: #ffffff;
  }
  * { margin: 0; padding: 0; box-sizing: border-box; }
  html, body {
    width: 902px; height: 1200px; overflow: hidden;
    background: var(--backdrop);
    font-family: "Questrial", "Century Gothic", sans-serif;
  }
  .sheet { position: relative; width: 902px; height: 1200px; }
  .card {
    position: absolute; left: 78px; width: 746px; height: 435px;
    border-radius: 22px; overflow: hidden;
  }
  .card--front { top: 132px; background: var(--panel-grey); }
  .card--back { top: 638px; background: var(--brand-blue); }

  .front-panel {
    position: absolute; left: 0; top: 0; bottom: 0; width: 420px;
    background: var(--brand-blue); color: var(--white);
  }
  .person { position: absolute; left: 48px; top: 58px; }
  .person__name { font-size: 30px; letter-spacing: 0.5px; line-height: 1; font-weight: 400; }
  .person__title { font-size: 18px; margin-top: 8px; }
  .person__credentials { font-size: 11px; margin-top: 12px; }

  .contacts { position: absolute; left: 48px; top: 320px; list-style: none; }
  .contacts li { display: flex; align-items: center; height: 22.5px; font-size: 17px; }
  .contacts svg { width: 12px; height: 12px; margin-right: 14px; flex: none; }

  .brand-name { font-weight: 400; letter-spacing: 1.5px; white-space: nowrap; }
  .brand-name--front {
    position: absolute; left: 612px; top: 358px; transform: translateX(-50%);
    font-size: 22px; color: var(--ink-dark);
  }
  .brand-name--back {
    position: absolute; left: 50%; top: 292px; transform: translateX(-50%);
    font-size: 34px; color: var(--white);
  }
</style>
</head>
<body>
<main class="sheet">
  <section class="card card--front" aria-label="Card front">
    <div class="front-panel">
      <div class="person">
        <h1 class="person__name">MARCUS DELLOW</h1>
        <p class="person__title">Structural Engineer</p>
        <p class="person__credentials">BEng(Hons), CPEng, CMengNZ, IntPE(NZ)</p>
      </div>
      <ul class="contacts">
        <li>
          <svg viewBox="0 0 12 12" aria-hidden="true"><path fill="#fff" d="M2.4 0.6l2 2.2-1 1.4c.7 1.6 1.9 2.8 3.5 3.5l1.4-1 2.2 2-1.2 1.9C5.6 10.4 1.6 6.4 0.6 1.8z"/></svg>
          0219364058
        </li>
        <li>
          <svg viewBox="0 0 12 12" aria-hidden="true"><rect x="0.5" y="2" width="11" height="8" fill="#fff"/><path d="M0.8 2.4L6 6.6l5.2-4.2" fill="none" stroke="#0f74bd" stroke-width="1"/></svg>
          marcus.dellow@keystoneaudit.co.nz
        </li>
        <li>
          <svg viewBox="0 0 12 12" aria-hidden="true"><circle cx="6" cy="6" r="5.5" fill="#fff"/><path d="M3 3.5c1 .2 1.6 1 1.4 2-.2.8.8 1.2.6 2.2M7.5 1.5c-.3 1 .4 1.6 1.2 1.8.8.2 1 1.2.6 2" fill="none" stroke="#0f74bd" stroke-width="1"/></svg>
          www.keystoneaudit.co.nz
        </li>
      </ul>
    </div>
    <p class="brand-name brand-name--front">KEYSTONE AUDIT</p>
  </section>

  <section class="card card--back" aria-label="Card back">
    <p class="brand-name brand-name--back">KEYSTONE AUDIT</p>
  </section>
</main>
</body>
</html>
```